Update our business cards to match our awesome new website

Need a new design for company business cards. We have recently revamped our website and would like our business cards to get a refresh too. I've uploaded the company artwork, logo, as well as the Branding Deck to better understand the look & feel of our brand. Please visit the website at hollowbrookestatesmi.com.

Industry/Entity Type

Real Estate

Contact Information for Business Card

must use the colors outlined in the Branding Deck uploaded to the site, or the colors of our logo.

Font styles to use
Other font styles liked:
• Calibri

Requirements
Must have
• Required items: Name, title, company logo, address: 218 Fenwick St. Suite 300, Elmridge, MI 48173, email address: cole@hollowbrookestatesMI.com, company phone 800-555-0193, cell: 555-555-0162
Nice to have
• a more simple design. not complicated
Should not have
• cartoonish characters, or whimsical writing or artwork, stay within our branding colors

```html
<!DOCTYPE html>
<html lang="en">
<head>
<meta charset="utf-8">
<title>Hollowbrook Estates – Business Card</title>
<link rel="stylesheet" href="https://fonts.googleapis.com/css2?family=Poppins:wght@400;500;600&display=swap">
<style>
  :root {
    --backdrop: #e8e5e0;
    --card: #ffffff;
    --ink: #231f20;
    --green: #4f9a45;
    --green-light: #62a84a;
    --green-dark: #3f8a3c;
    --blue: #2f7fcb;
    --blue-dark: #1f6fbe;
    --white: #ffffff;
  }
  * { margin: 0; padding: 0; box-sizing: border-box; }
  html, body {
    width: 900px;
    height: 1200px;
    overflow: hidden;
    background: var(--backdrop);
    font-family: "Poppins", sans-serif;
  }
  .card {
    position: absolute;
    left: 80px;
    width: 733px;
    height: 429px;
    background: var(--card);
    border-radius: 22px;
    overflow: hidden;
    box-shadow: 0 6px 16px rgba(0,0,0,0.25);
  }
  .card--front { top: 128px; }
  .card--back { top: 645px; }
  .card__shapes {
    position: absolute;
    inset: 0;
    width: 733px;
    height: 429px;
  }
  .holder { position: absolute; left: 52px; top: 54px; }
  .holder__name {
    font-weight: 600;
    font-size: 28px;
    line-height: 1.2;
    color: var(--ink);
  }
  .holder__title {
    font-weight: 400;
    font-size: 19px;
    color: var(--green-dark);
    margin-top: 2px;
  }
  .brand {
    position: absolute;
    color: var(--ink);
    font-weight: 500;
    text-align: right;
    text-transform: uppercase;
    letter-spacing: 0.5px;
  }
  .brand__name { font-size: 29px; line-height: 1; white-space: nowrap; }
  .brand__suffix {
    font-size: 11px;
    text-transform: none;
    letter-spacing: 0;
    margin-top: 6px;
  }
  .card--front .brand { right: 40px; top: 128px; }
  .card--back .brand { left: 0; right: 0; top: 236px; text-align: center; }
  .card--back .brand__name { font-size: 33px; }
  .card--back .brand__suffix { text-align: right; padding-right: 160px; }
  .contacts {
    position: absolute;
    left: 50px;
    top: 218px;
    list-style: none;
  }
  .contact {
    display: flex;
    align-items: center;
    gap: 14px;
    margin-bottom: 13px;
    color: var(--white);
    font-size: 15.5px;
    line-height: 25px;
  }
  .contact__icon {
    width: 40px;
    height: 40px;
    flex: none;
  }
  .site-url {
    position: absolute;
    left: 47px;
    top: 385px;
    color: var(--white);
    font-size: 15px;
    font-weight: 500;
  }
</style>
</head>
<body>

<section class="card card--front" aria-label="Business card front">
  <svg class="card__shapes" viewBox="0 0 733 429" aria-hidden="true">
    <defs>
      <linearGradient id="green-sweep" x1="0" y1="0" x2="1" y2="1">
        <stop offset="0" stop-color="#3f8a3c"/>
        <stop offset="1" stop-color="#62a84a"/>
      </linearGradient>
      <linearGradient id="blue-sweep" x1="0" y1="0" x2="1" y2="1">
        <stop offset="0" stop-color="#4a93d6"/>
        <stop offset="1" stop-color="#1f6fbe"/>
      </linearGradient>
    </defs>
    <path d="M120,152 C400,188 620,322 733,398 L733,429 L708,429 C560,300 360,185 120,152 Z" fill="url(#blue-sweep)"/>
    <path d="M0,140 C250,148 500,275 645,429 L0,429 Z" fill="url(#green-sweep)"/>
  </svg>

  <div class="holder">
    <h1 class="holder__name">Cole Whitaker</h1>
    <p class="holder__title">Managing Director</p>
  </div>

  <div class="brand">
    <div class="brand__name">Hollowbrook Estates</div>
    <div class="brand__suffix">of Michigan, LLC</div>
  </div>

  <ul class="contacts">
    <li class="contact">
      <svg class="contact__icon" viewBox="0 0 40 40" aria-hidden="true">
        <circle cx="20" cy="20" r="18" fill="#ffffff"/>
        <circle cx="20" cy="20" r="14.5" fill="#4f9a45"/>
        <path d="M15 12.5c1-.6 1.9-.3 2.4.6l1.3 2.4c.4.8.2 1.6-.5 2.1l-.9.6c.7 1.7 2 3.1 3.6 3.9l.6-.9c.5-.7 1.4-.9 2.1-.5l2.4 1.3c.9.5 1.2 1.5.6 2.4l-.7 1c-.8 1.2-2.3 1.6-3.6 1-4.3-1.8-7.6-5.2-9.4-9.5-.5-1.3-.1-2.8 1.1-3.6z" fill="#ffffff"/>
      </svg>
      <span>Office: 800-555-0193<br>Cell: 555-555-0162</span>
    </li>
    <li class="contact">
      <svg class="contact__icon" viewBox="0 0 40 40" aria-hidden="true">
        <circle cx="20" cy="20" r="18" fill="#ffffff"/>
        <circle cx="20" cy="20" r="14.5" fill="#4f9a45"/>
        <g fill="none" stroke="#ffffff" stroke-width="1.4">
          <circle cx="20" cy="20" r="8"/>
          <ellipse cx="20" cy="20" rx="3.5" ry="8"/>
          <line x1="12" y1="20" x2="28" y2="20"/>
          <path d="M13.5 15.5h13M13.5 24.5h13"/>
        </g>
      </svg>
      <span>hollowbrookestatesmi.com<br>cole@hollowbrookestatesMI.com</span>
    </li>
    <li class="contact">
      <svg class="contact__icon" viewBox="0 0 40 40" aria-hidden="true">
        <circle cx="20" cy="20" r="18" fill="#ffffff"/>
        <circle cx="20" cy="20" r="14.5" fill="#4f9a45"/>
        <path d="M20 11a6.5 6.5 0 0 0-6.5 6.5c0 4.6 6.5 11.5 6.5 11.5s6.5-6.9 6.5-11.5A6.5 6.5 0 0 0 20 11zm0 9a2.5 2.5 0 1 1 0-5 2.5 2.5 0 0 1 0 5z" fill="#ffffff"/>
      </svg>
      <span>218 Fenwick St. Suite 300<br>Elmridge, MI 48173</span>
    </li>
  </ul>
</section>

<section class="card card--back" aria-label="Business card back">
  <svg class="card__shapes" viewBox="0 0 733 429" aria-hidden="true">
    <path d="M0,344 C260,340 480,372 615,429 L588,429 C460,380 260,352 0,351 Z" fill="#4f9a45"/>
    <path d="M0,357 C230,357 420,378 520,429 L0,429 Z" fill="#1f6fbe"/>
  </svg>

  <div class="brand">
    <div class="brand__name">Hollowbrook Estates</div>
    <div class="brand__suffix">of Michigan, LLC</div>
  </div>

  <p class="site-url">www.hollowbrookestatesmi.com</p>
</section>

</body>
</html>
```